NLC Rio Verde Norte Artist Corinna Whitlatch event

Corinna Whitlatch

Elevate your appreciation for the arts with an Only-in-NLC VIP tour of the priceless art collection of El Paso's mysterious Corinna, including access to her museum which is not open to the public. Dinner and transportation between sites included.

Corinna Whitlatch lives and works in El Paso, Texas. Praised by the Harbor Ledger Daily as "fresh," "a tough act to follow," and the "ultimate in transgression," Whitlatch is widely recognized in her home state of Texas as a unique presence and highly original artist. She has been characterized by Delia Frank, former curator at the Bayridge Gallery of Fine Work, as "an anachronism who earnestly pursues a long-held tradition of landscape and genre painting . . . inspired by her Southwestern environment and vivid imagination.

Rendered with thick applications of radiant colors, Whitlatch's paintings are intensely personal, dream-like explorations of the natural world.
DATE: Wednesday, September 26, 2018
VENUE: RIVERBEND CIVIC TRUST HALL
718 W Tamsin Ave
El Paso, TX 79948
United States
AGENDA: 6:00 - 7:30 Light supper and orientation to the mysterious Corinna Whitlatch, Riverbend Civic Trust Hall downtown
7:30 - 7:45 Board van to go to Sunward Health Campus Corinna Whitlatch Chapel
7:45 - 8:15 View Chapel
8:15 - 8:30 Board van to go to Museum Whitlatch
8:30 - 9:15 View Museum Whitlatch with dessert
9:15 - 9:30 Return downtown
RESOURCE(S): Tessa Brund - Being an icon in the art world, and not needing any introduction, Tessa probably knows more about Corinna Whitlatch than anyone!

Wade Hollins – President and CEO of the Riverbend Civic Trust since 2011

Lorinda Vasko - Director of Presentations of the Corinna Whitlatch Museum and an art history graduate of GSVC

Owen Strade - Nobody has ever actually seen Corinna Whitlatch, yet ophthalmologist and NLC member Dr. Owen Strade is her eye surgeon. How can that be? Find out at the event!
ATTENDANCE: NLC Members, NLC Spouses/Guests, NLC SAGE Members, NLC SAGE Spouses/Guests
ATTIRE: Business Casual
DAY CHAIRS: Owen Strade
Tessa Brund

Invite 5x7 or 7x5 please

Target Market(s)

NLC Rio Verde Norte Members

Industry/Entity Type

Non Profit

Font styles to use
Decorative
Script

Colors

Designer to choose colors to be used in the design.

Requirements
Must have
• Event title
• Date
• Artist description (Corinna Whitlatch)
• Venue
• Attire
• Attendees
• Logos
Nice to have
• Information about the artist
Should not have
• Art from another artists

```html
<!DOCTYPE html>
<html lang="en">
<head>
<meta charset="utf-8">
<title>Corinna Whitlatch — NLC Rio Verde Norte</title>
<link rel="stylesheet" href="https://fonts.googleapis.com/css2?family=Inter:wght@400;700&family=Playball&display=swap">
<style>
  :root {
    --ink: #3a3a3a;
    --ink-soft: #2e2e2e;
    --amber: #f8ad0c;
    --paper: #ffffff;
    --title: #ffffff;
  }
  * { box-sizing: border-box; margin: 0; padding: 0; }
  html, body { width: 857px; height: 1200px; overflow: hidden; background: var(--paper); }
  .invite {
    position: relative;
    width: 857px;
    height: 1200px;
    overflow: hidden;
    font-family: "Inter", Helvetica, Arial, sans-serif;
    color: var(--ink);
  }
  .watercolor {
    position: absolute;
    left: 0; top: 0;
    width: 857px; height: 1024px;
    background:
      radial-gradient(ellipse 180px 120px at 90% 6%, rgba(60,90,200,0.55), transparent 70%),
      radial-gradient(ellipse 220px 140px at 62% 4%, rgba(230,60,140,0.55), transparent 70%),
      radial-gradient(ellipse 200px 150px at 35% 8%, rgba(240,80,110,0.45), transparent 70%),
      radial-gradient(ellipse 160px 120px at 10% 6%, rgba(250,220,40,0.8), transparent 70%),
      radial-gradient(ellipse 200px 170px at 80% 22%, rgba(235,70,110,0.45), transparent 70%),
      radial-gradient(ellipse 160px 200px at 96% 40%, rgba(60,150,110,0.4), transparent 70%),
      radial-gradient(ellipse 260px 160px at 88% 55%, rgba(240,110,120,0.4), transparent 70%),
      radial-gradient(ellipse 260px 200px at 15% 35%, rgba(248,150,30,0.55), transparent 70%),
      linear-gradient(180deg, #fbe25a 0%, #fbcf3e 30%, #f9b526 60%, var(--amber) 85%, var(--amber) 100%);
  }
  .intro {
    position: absolute;
    top: 226px;
    left: 86px;
    width: 686px;
    display: flex;
    justify-content: space-between;
    font-size: 15.2px;
    line-height: 25.2px;
    color: var(--ink-soft);
  }
  .intro-col { width: 322px; text-align: justify; }
  .drop-cap {
    float: left;
    font-size: 124px;
    line-height: 90px;
    font-weight: 400;
    color: var(--ink);
    margin: 7px 8px 0 -2px;
  }
  .event-title {
    position: absolute;
    left: 0; top: 512px;
    width: 857px;
    text-align: center;
    font-family: "Playball", cursive;
    color: var(--title);
    font-size: 142px;
    line-height: 110px;
    font-weight: 400;
  }
  .pitch {
    position: absolute;
    left: 117px; top: 826px;
    width: 606px;
    font-size: 20.5px;
    line-height: 33.5px;
    font-weight: 700;
    text-align: justify;
    color: var(--ink);
  }
  .details {
    position: absolute;
    left: 123px; top: 1040px;
    font-size: 13.8px;
    line-height: 20px;
    color: var(--ink-soft);
  }
  .details dt { display: inline; font-weight: 700; }
  .details dd { display: inline; }
  .details .row { display: block; }
  .details .indent { display: block; padding-left: 112px; }
  .brand {
    position: absolute;
    right: 86px; bottom: 30px;
    display: flex;
    align-items: center;
    gap: 8px;
    font-size: 13.8px;
    font-weight: 700;
    color: var(--ink-soft);
  }
  .brand-dot { width: 14px; height: 14px; border-radius: 50%; background: var(--amber); }
</style>
</head>
<body>
<main class="invite">
  <div class="watercolor" role="img" aria-label="Bright abstract watercolor wash in yellow, pink, blue and green fading into a warm amber field"></div>

  <section class="intro">
    <p class="intro-col"><span class="drop-cap">C</span>orinna Whitlatch lives and works in El Paso, Texas. Praised by the Harbor Ledger Daily as “fresh,” “a tough act to follow,” and the “ultimate in transgression,” Whitlatch is widely recognized in her home state of Texas as a unique presence and highly original artist. She has been characterized by Delia Frank, former curator at the Bayridge Gallery of Fine Work, as “an anachronism who</p>
    <div class="intro-col">
      <p>earnestly pursues a long-held tradition of landscape and genre painting . . . inspired by her Southwestern environment and vivid imagination.</p>
      <p>Rendered with thick applications of radiant colors, Whitlatch’s paintings are intensely personal, dream-like explorations of the natural world.</p>
    </div>
  </section>

  <h1 class="event-title">Corinna<br>Whitlatch</h1>

  <p class="pitch">Elevate your appreciation for the arts with an Only-in-NLC VIP tour of the PRICELESS ART COLLECTION of EL PASO’S MYSTERIOUS CORINNA, including access to her museum which is not open to the public. Dinner and transportation between sites included.</p>

  <dl class="details">
    <div class="row"><dt>DATE:</dt> <dd>Wednesday, September 26, 2018</dd></div>
    <div class="row"><dt>VENUE:</dt> <dd>Riverbend Civic Trust Hall, 718 W Tamsin Ave, El Paso, TX 79948</dd></div>
    <div class="row"><dt>ATTENDANCE:</dt> <dd>NLC Members, NLC Spouses/Guests,</dd></div>
    <div class="indent">NLC SAGE Members, NLC SAGE Spouses/Guests</div>
    <div class="row"><dt>ATTIRE:</dt> <dd>Business Casual</dd></div>
    <div class="row"><dt>DAY CHAIRS:</dt> <dd>Owen Strade, Tessa Brund</dd></div>
  </dl>

  <div class="brand"><span class="brand-dot"></span><span>NLC Rio Verde Norte</span></div>
</main>
</body>
</html>
```